Simple fencing and steel manufacturing website

** update 01/04/2015 ** we did not add logo design, but if your font/logo is accepted we will add $50 to make it more fair
Even if you web design is not chosen, but your logo is, we will pay you $50. If both are chosen you will get an extra $50
Open brief

Site map:
Home
About
Gallery
-photos
-testimonials
Contact

No current website:

No current logo, colors currently black and gold but we don't mind changing them - wide open brief
Happy for new font/style/logo for company name which is Paling Brightway

Customer wants clean, credible and professional look & feel
stock photos OK

Brief:

One home page - simple with 2 or 3 small areas to tease and attract the user and one template page to suit all the other pages

All competitor websites are pretty bad, the best of them is
http://www.wexmoorrailing.com.au/index.html

Target Market(s)

Government and top level builders

Industry/Entity Type

Fencing

Requirements
Must have
• 1. Display ISO and environmental awards (ISO9001 AS4801 ISO14001)
• 2. A list of about 15 products
• Can be in teaser areas of home page as suggested before or slider or really anywhere
Nice to have
• Log with name - nice but not necessary (we don't have one)

```html
<!DOCTYPE html>
<html lang="en">
<head>
<meta charset="utf-8">
<title>Paling Brightway — Home</title>
<link href="https://fonts.googleapis.com/css2?family=Advent+Pro:wght@300;400;500&family=Arimo:wght@400;700&display=swap" rel="stylesheet">
<style>
:root{
  --green:#55b21e;
  --green-section:#66ad1e;
  --black:#000;
  --nav-bg:rgba(20,20,20,.85);
  --purple:#30285e;
  --purple-dark:#28214f;
  --orange:#e47517;
  --orange-dark:#b0590f;
  --pink:#ee2f5e;
  --pink-dark:#c3254c;
  --teal:#0c3d52;
  --footer-nav:#2e2e2e;
  --footer-base:#1b1b1b;
  --white:#fff;
  --muted:#bdbdbd;
}
*{box-sizing:border-box;margin:0;padding:0}
html,body{width:758px;height:1200px;overflow:hidden;background:#000}
body{font-family:"Arimo",Arial,sans-serif;color:var(--white);position:relative}
.display{font-family:"Advent Pro",sans-serif}
a{color:inherit;text-decoration:none}

/* Header */
.site-header{position:absolute;top:0;left:0;width:758px;height:28px;background:var(--nav-bg);z-index:3}
.brand{position:absolute;left:70px;top:4px;font-family:"Advent Pro",sans-serif;font-size:17px;font-weight:400;color:var(--white)}
.main-nav{position:absolute;left:189px;top:0;height:28px;display:flex;align-items:center;gap:11px;border-left:1px solid #444;padding-left:8px}
.main-nav a{font-size:7px;font-weight:700;text-transform:uppercase}
.main-nav a.active{color:var(--green)}
.search{position:absolute;left:586px;top:5px;width:101px;height:18px;background:#3a3a3a;border:1px solid #4a4a4a;font-size:7px;color:#888;padding:5px 6px}
.search svg{position:absolute;right:5px;top:4px}

/* Hero */
.hero{position:absolute;top:0;left:0;width:758px;height:402px}
.hero-photo{position:absolute;inset:0;background:radial-gradient(ellipse at 35% 45%,#5a5856 0%,#2e2d2c 45%,#111 100%)}
.hero-copy{position:absolute;left:478px;top:136px;width:232px}
.hero-title{font-family:"Advent Pro",sans-serif;font-weight:300;font-size:33px;line-height:36px}
.hero-text{font-size:9.2px;font-weight:700;line-height:14px;margin-top:5px;padding-left:3px;width:216px}
.btn-primary{position:absolute;left:3px;top:93px;width:132px;height:24px;background:var(--green);font-size:7.5px;font-weight:700;display:flex;align-items:center;justify-content:center;gap:5px;text-transform:uppercase}
.hero-arrow{position:absolute;top:187px}

/* Explore */
.explore-heading{position:absolute;top:402px;left:0;width:758px;height:32px;background:var(--black);text-align:center;font-size:25px;font-weight:400;line-height:32px}
.tiles{position:absolute;top:434px;left:0;width:758px;height:369px;display:flex}
.tile{flex:1;position:relative}
.tile-visual{height:256px;display:flex;align-items:center;justify-content:center}
.tile-body{height:113px;padding:10px 6px 0 6px;position:relative}
.tile-title{font-family:"Advent Pro",sans-serif;font-size:20px;font-weight:400;text-transform:uppercase;line-height:22px}
.tile-text{font-size:6.4px;margin-top:7px;padding-left:2px}
.btn-explore{position:absolute;right:10px;top:76px;width:73px;height:23px;font-size:7.5px;font-weight:700;display:flex;align-items:center;justify-content:center;gap:5px;text-transform:uppercase}
.tile--projects .tile-visual{background:var(--purple)}
.tile--projects .tile-body{background:var(--purple-dark)}
.tile--projects .btn-explore{background:#3b3270}
.tile--advantage .tile-visual{background:var(--orange)}
.tile--advantage .tile-body{background:var(--orange-dark)}
.tile--advantage .btn-explore{background:var(--orange)}
.tile--contact .tile-visual{background:var(--pink)}
.tile--contact .tile-body{background:var(--pink-dark)}
.tile--contact .btn-explore{background:var(--pink)}

/* Products */
.products{position:absolute;top:803px;left:0;width:758px;height:221px;background:var(--green-section)}
.products-tab{position:absolute;left:363px;top:-12px}
.products-title{position:absolute;top:22px;width:100%;left:-2px;text-align:center;font-size:27px;font-weight:400;text-transform:uppercase}
.products-intro{position:absolute;top:55px;left:0;width:758px;text-align:center;font-size:7.4px}
.product-list{position:absolute;top:94px;list-style:none}
.product-list li{font-size:6.4px;height:15.2px}
.product-list li::before{content:"»";color:#b5dc8c;margin-right:5px}
.quality-seal{position:absolute;left:557px;top:37px;width:163px;height:163px;border-radius:50%;background:radial-gradient(circle,#e9c24a 0%,#c99a2e 55%,#8a6a22 100%)}

/* Standards */
.standards{position:absolute;top:1024px;left:0;width:758px;height:107px;background:var(--teal)}
.standards-quote{position:absolute;left:70px;top:16px;font-size:26px;font-weight:300;line-height:31px}
.cert-panel{position:absolute;left:496px;top:13px;width:190px;height:82px;background:var(--white);border-radius:4px;display:flex;justify-content:space-around;align-items:center;padding:0 6px}
.cert{width:44px;height:68px;border-radius:2px}
.cert--quality{background:linear-gradient(#fff 0 18%,#d8262e 18% 72%,#fff 72%)}
.cert--environment{background:linear-gradient(#fff 0 18%,#1f8a3c 18% 72%,#fff 72%)}
.cert--ohs{background:linear-gradient(#fff 0 18%,#f3b31a 18% 72%,#fff 72%)}

/* Footer */
.footer-nav{position:absolute;top:1131px;left:0;width:758px;height:37px;background:var(--footer-nav);display:flex;justify-content:center;align-items:center;gap:15px}
.footer-nav a{font-size:6.4px;color:var(--muted);text-transform:uppercase}
.footer-base{position:absolute;top:1168px;left:0;width:758px;height:32px;background:var(--footer-base)}
.copyright{position:absolute;left:70px;top:13px;font-size:6.4px;color:#8a8a8a}
.footer-brand{position:absolute;right:72px;top:4px;font-family:"Advent Pro",sans-serif;font-size:18px;color:var(--white)}
.to-top{position:absolute;left:730px;top:5px;width:21px;height:21px;background:#000;font-size:6px;font-weight:700;display:flex;align-items:center;justify-content:center}
</style>
</head>
<body>

<section class="hero">
  <div class="hero-photo" role="img" aria-label="Close-up photograph of dark woven steel mesh fencing"></div>
  <svg class="hero-arrow" style="left:30px" width="16" height="28" viewBox="0 0 16 28"><polyline points="14,1 2,14 14,27" fill="none" stroke="#7fc93a" stroke-width="1.5"/></svg>
  <svg class="hero-arrow" style="left:714px" width="16" height="28" viewBox="0 0 16 28"><polyline points="2,1 14,14 2,27" fill="none" stroke="#7fc93a" stroke-width="1.5"/></svg>
  <div class="hero-copy">
    <h1 class="hero-title">Title goes here</h1>
    <p class="hero-text">Lorem ipsum dolor sit amet consecutor. Lorem ipsum. Lorem ipsum dolor sit amet consecutor. Lorem ipsum</p>
    <a class="btn-primary" href="#">
      <svg width="11" height="9" viewBox="0 0 11 9" fill="#fff"><rect x="0" y="0" width="2" height="2"/><rect x="3" y="0" width="8" height="2"/><rect x="0" y="3.5" width="2" height="2"/><rect x="3" y="3.5" width="8" height="2"/><rect x="0" y="7" width="2" height="2"/><rect x="3" y="7" width="8" height="2"/></svg>
      View our products
    </a>
  </div>
</section>

<header class="site-header">
  <a class="brand" href="#">Paling Brightway</a>
  <nav class="main-nav">
    <a class="active" href="#">Home</a>
    <a href="#">About us</a>
    <a href="#">Gallery</a>
    <a href="#">Projects</a>
    <a href="#">Contact us</a>
  </nav>
  <div class="search">Search
    <svg width="9" height="9" viewBox="0 0 9 9"><circle cx="3.7" cy="3.7" r="2.8" fill="none" stroke="#999" stroke-width="1.2"/><line x1="5.8" y1="5.8" x2="8.5" y2="8.5" stroke="#999" stroke-width="1.4"/></svg>
  </div>
</header>

<h2 class="explore-heading display">Explore Us</h2>

<section class="tiles">
  <article class="tile tile--projects">
    <div class="tile-visual">
      <svg width="72" height="92" viewBox="0 0 72 92" fill="none" stroke="#fff" stroke-width="5" stroke-linecap="round" stroke-linejoin="round">
        <rect x="4" y="10" width="64" height="78" rx="9"/>
        <path d="M24 10 v-3 a12 8 0 0 1 24 0 v3 z" fill="#fff"/>
        <polyline points="16,32 21,37 29,27"/><line x1="36" y1="32" x2="56" y2="32"/>
        <polyline points="16,50 21,55 29,45"/><line x1="36" y1="50" x2="56" y2="50"/>
        <polyline points="16,68 21,73 29,63"/><line x1="36" y1="68" x2="56" y2="68"/>
      </svg>
    </div>
    <div class="tile-body">
      <h3 class="tile-title">Our Projects</h3>
      <p class="tile-text">Lorem ipsum dolor sit amet consecutor. Lorem ipsum dolor sit amet consecutor.</p>
      <a class="btn-explore" href="#"><svg width="9" height="9" viewBox="0 0 9 9" fill="none" stroke="#fff" stroke-width="1.3"><path d="M4 1H1v7h7V5"/><path d="M5 1h3v3M8 1 4 5"/></svg>Explore</a>
    </div>
  </article>
  <article class="tile tile--advantage">
    <div class="tile-visual">
      <svg width="98" height="74" viewBox="0 0 120 90" role="img" aria-label="Handshake icon">
        <polygon points="0,22 18,14 36,52 18,60" fill="#fff"/>
        <polygon points="120,22 102,14 84,52 102,60" fill="#fff"/>
        <path d="M32 26 L58 15 Q66 12 74 17 L97 25 L86 52 L64 74 Q58 80 52 74 L40 62 Z" fill="#fff"/>
        <g stroke="#e47517" stroke-width="3" stroke-linecap="round" fill="none">
          <path d="M62 20 Q54 30 64 35 L78 28"/>
          <line x1="42" y1="56" x2="51" y2="47"/>
          <line x1="48" y1="64" x2="57" y2="55"/>
          <line x1="55" y1="71" x2="64" y2="62"/>
        </g>
      </svg>
    </div>
    <div class="tile-body">
      <h3 class="tile-title">Our Advantage</h3>
      <p class="tile-text">Lorem ipsum dolor sit amet consecutor. Lorem ipsum dolor sit amet consecutor.</p>
      <a class="btn-explore" href="#"><svg width="9" height="9" viewBox="0 0 9 9" fill="none" stroke="#fff" stroke-width="1.3"><path d="M4 1H1v7h7V5"/><path d="M5 1h3v3M8 1 4 5"/></svg>Explore</a>
    </div>
  </article>
  <article class="tile tile--contact">
    <div class="tile-visual">
      <svg width="58" height="82" viewBox="0 0 58 82"><path d="M29 82 C20 66 0 48 0 29 A29 29 0 0 1 58 29 C58 48 38 66 29 82Z" fill="#fff"/><circle cx="29" cy="28" r="11" fill="#ee2f5e"/></svg>
    </div>
    <div class="tile-body">
      <h3 class="tile-title">Contact Us</h3>
      <p class="tile-text">Lorem ipsum dolor sit amet consecutor. Lorem ipsum dolor sit amet consecutor.</p>
      <a class="btn-explore" href="#"><svg width="9" height="9" viewBox="0 0 9 9" fill="none" stroke="#fff" stroke-width="1.3"><path d="M4 1H1v7h7V5"/><path d="M5 1h3v3M8 1 4 5"/></svg>Explore</a>
    </div>
  </article>
</section>

<section class="products">
  <svg class="products-tab" width="32" height="14" viewBox="0 0 32 14"><path d="M0 14 A16 14 0 0 1 32 14Z" fill="#66ad1e"/><polygon points="12,10 16,6 20,10" fill="#fff"/></svg>
  <h2 class="products-title display">Our Products</h2>
  <p class="products-intro">Lorem ipsum dolor sit amet consecutor Lorem ipsum dolor sit amet consecutor.</p>
  <ul class="product-list" style="left:72px">
    <li>Product Link 1</li><li>Product Link 2</li><li>Product Link 3</li><li>Product Link 4</li><li>Product Link 5</li>
  </ul>
  <ul class="product-list" style="left:206px">
    <li>Product Link 1</li><li>Product Link 2</li><li>Product Link 3</li><li>Product Link 4</li><li>Product Link 5</li>
  </ul>
  <ul class="product-list" style="left:341px">
    <li>Product Link 1</li><li>Product Link 2</li><li>Product Link 3</li><li>Product Link 4</li><li>Product Link 5</li>
  </ul>
  <div class="quality-seal" role="img" aria-label="Gold high quality guarantee seal illustration"></div>
</section>

<section class="standards">
  <p class="standards-quote display">Our commitment to Quality, Environmental<br>and OHS standards is your guarantee.</p>
  <div class="cert-panel">
    <div class="cert cert--quality" role="img" aria-label="Quality management certification badge"></div>
    <div class="cert cert--environment" role="img" aria-label="Environmental management certification badge"></div>
    <div class="cert cert--ohs" role="img" aria-label="Occupational health and safety certification badge"></div>
  </div>
</section>

<nav class="footer-nav">
  <a href="#">Home</a><a href="#">About us</a><a href="#">Gallery</a><a href="#">Projects</a><a href="#">Contact us</a>
</nav>
<footer class="footer-base">
  <p class="copyright">Copyright © 2015 Paling Brightway. All rights reserved.</p>
  <span class="footer-brand">Paling Brightway</span>
  <a class="to-top" href="#">TOP</a>
</footer>

</body>
</html>
```